Design some Business Cards for Kestrel Data Works

I would like a nicely designed business card template for my re-branded business, 'Kestrel Data Works'.

I would like it to be a standard landscape design to fit on 88.5*50mm PVC plastic cards:

I've attached our business logo files, if the design could match their style and color scheme while making good aesthetic use of the transparent plastic medium they will be printed on that would be fantastic.

```html
<!DOCTYPE html>
<html lang="en">
<head>
<meta charset="utf-8">
<title>Kestrel Data Works – Business Card</title>
<link href="https://fonts.googleapis.com/css2?family=Open+Sans:wght@300;400;600&display=swap" rel="stylesheet">
<style>
  :root {
    --page-bg: #1f2022;
    --frost-light: #c3c6ca;
    --frost-dark: #9ea2a7;
    --band-blue: #333f9a;
    --band-green: #7fd13b;
    --brand-blue: #2b73b8;
    --brand-green: #6cc63a;
    --ink: #34373c;
    --name-ink: #e4e7f3;
  }
  html, body {
    margin: 0;
    width: 1200px;
    height: 800px;
    overflow: hidden;
    background: var(--page-bg);
    font-family: "Open Sans", Arial, sans-serif;
  }
  .card {
    position: absolute;
    left: 150px;
    top: 146px;
    width: 900px;
    height: 508px;
    border-radius: 26px;
    overflow: hidden;
    background: linear-gradient(160deg, var(--frost-light), var(--frost-dark));
  }
  .card-bands {
    position: absolute;
    inset: 0;
  }
  .contact-list {
    position: absolute;
    left: 70px;
    top: 178px;
    margin: 0;
    padding: 0;
    list-style: none;
    color: var(--ink);
    font-size: 19px;
    line-height: 31px;
  }
  .contact-list li {
    display: flex;
    align-items: center;
    gap: 12px;
  }
  .contact-icon {
    width: 18px;
    height: 18px;
    flex: none;
  }
  .brand {
    position: absolute;
    left: 468px;
    top: 188px;
    display: flex;
    align-items: center;
    gap: 16px;
  }
  .brand-dot {
    width: 46px;
    height: 46px;
    border-radius: 50%;
    background: var(--brand-green);
  }
  .brand-name {
    color: var(--brand-blue);
    font-weight: 600;
    font-size: 42px;
    line-height: 46px;
    letter-spacing: -0.5px;
  }
  .holder {
    position: absolute;
    right: 66px;
    bottom: 28px;
    text-align: right;
    color: var(--name-ink);
  }
  .holder-name {
    font-weight: 300;
    font-size: 28px;
    line-height: 32px;
  }
  .holder-role {
    font-weight: 300;
    font-size: 16px;
    line-height: 20px;
    opacity: 0.85;
  }
</style>
</head>
<body>
  <div class="card">
    <svg class="card-bands" viewBox="0 0 900 508" width="900" height="508">
      <path d="M0,0 H360 Q150,20 0,110 Z" fill="var(--band-blue)"/>
      <path d="M0,110 Q150,20 360,0 L405,0 Q170,36 0,128 Z" fill="var(--band-green)"/>
      <path d="M0,385 Q450,440 900,376 L900,400 Q450,456 0,396 Z" fill="var(--band-green)"/>
      <path d="M0,396 Q450,456 900,400 V508 H0 Z" fill="var(--band-blue)"/>
    </svg>

    <ul class="contact-list">
      <li>
        <svg class="contact-icon" viewBox="0 0 18 18"><path d="M4 2 L7 2 L8 6 L6 7.5 Q7.5 10.5 10.5 12 L12 10 L16 11 L16 14 Q16 16 14 16 Q3 15 2 4 Q2 2 4 2 Z" fill="var(--ink)"/></svg>
        <span>555 014 2290</span>
      </li>
      <li>
        <svg class="contact-icon" viewBox="0 0 18 18"><rect x="1.5" y="4" width="15" height="10" rx="1.5" fill="var(--ink)"/><path d="M2 5 L9 10 L16 5" stroke="var(--frost-light)" stroke-width="1.4" fill="none"/></svg>
        <span>emarlow@kestreldataworks.com</span>
      </li>
      <li>
        <svg class="contact-icon" viewBox="0 0 18 18"><circle cx="9" cy="9" r="7.5" fill="none" stroke="var(--ink)" stroke-width="1.6"/><ellipse cx="9" cy="9" rx="3.2" ry="7.5" fill="none" stroke="var(--ink)" stroke-width="1.3"/><path d="M1.5 9 H16.5" stroke="var(--ink)" stroke-width="1.3"/></svg>
        <span>www.kestreldataworks.com</span>
      </li>
      <li>
        <svg class="contact-icon" viewBox="0 0 18 18"><path d="M9 1 Q15 1 15 7 Q15 11 9 17 Q3 11 3 7 Q3 1 9 1 Z" fill="var(--ink)"/><circle cx="9" cy="7" r="2.2" fill="var(--frost-light)"/></svg>
        <span>Address line1, Adress line2</span>
      </li>
    </ul>

    <div class="brand">
      <div class="brand-dot"></div>
      <div class="brand-name">Kestrel<br>Data Works</div>
    </div>

    <div class="holder">
      <div class="holder-name">Ellis Marlow</div>
      <div class="holder-role">Marketing Manager</div>
    </div>
  </div>
</body>
</html>
```